Security company needs a business card design

We have a logo & we provide security services specialising in the construction site industry & remote areas. We are looking for a modern design preferably hi-tech as we provide hi-end specialised security services. We do not do pubs, clubs etc. Many of our employees are ex defence force & are highly qualified in covert ops etc.

Below are details that we would like on the front of the business card (I have attached our logo)
Logo + ML 738204519 (ML is abbreviation for "Master License")
We are also members of "GRONT" not sure if we need to put their logo on the business card or just make a reference to our membership (please advise - I have also attached their logo)

Company name: Vantor Ridge Security Services Pty Ltd

1) Employee name: Darren Okafor
Designation: Security Advisor / Director
Contact: M: 0451 307 984
e:darren@vantorridgesecurity-example.com.au (500cards 1st order)
2) Employee name: Gregory Okafor
Designation: Manager
Contact: M: 0437 215 640
e:gregory@vantorridgesecurity-example.com.au (250cards 1st order)
3) a generic card with no employee name or designation (250cards 1st order)

Company Address: 612 Wattlebend Rd, Coffs Harbour NSW 2450
T: +61 2 6621 4093 F: +61 2 6621 4058
E:admin@vantorridgesecurity-example.com.au
www.vantorridgesecurity-example.com.au

Below are details we provide which have been placed previously on the back of our business card:
Static Guards; Mobile Vehicle patrols; Alarm monitoring; 3 G CCTV Monitoring; Specialists in providing security requirements for construction sites & remote areas.
Updates

                                        Refer new pdf just uploaded

Target Market(s)

Security required for construction sites & remote areas

Industry/Entity Type

Construction

```html
<!DOCTYPE html>
<html lang="en">
<head>
<meta charset="utf-8">
<title>Vantor Ridge Security Services – Business Cards</title>
<link href="https://fonts.googleapis.com/css2?family=Maven+Pro:wght@400;500;700&display=swap" rel="stylesheet">
<style>
  :root {
    --stage: #1c1c1e;
    --navy-deep: #262c86;
    --navy: #2b3a98;
    --blue-mid: #1d6fcf;
    --cyan: #19a7e2;
    --band: #2db4ea;
    --accent: #3cbcf2;
    --ink: #1f2a7a;
    --white: #ffffff;
    --badge: #c9d24a;
  }
  * { margin: 0; padding: 0; box-sizing: border-box; }
  html, body { width: 1200px; height: 900px; overflow: hidden; background: var(--stage); }
  body { position: relative; font-family: "Maven Pro", sans-serif; }

  .card { position: absolute; width: 496px; height: 300px; overflow: hidden; }
  .card--front { left: 93px; top: 135px;
    background: radial-gradient(ellipse 55% 60% at 50% 42%, var(--blue-mid) 0%, var(--navy) 55%, var(--navy-deep) 100%); }
  .card--back { background: linear-gradient(90deg, var(--cyan) 0%, #2280d4 40%, var(--navy) 75%, var(--navy-deep) 100%); }
  .card--gregory { left: 612px; top: 135px; }
  .card--darren { left: 93px; top: 466px; }
  .card--generic { left: 612px; top: 466px; }

  .info-band { position: absolute; left: 0; right: 0; top: 142px; height: 71px; background: var(--band); opacity: .92; }

  .brand-mark { position: absolute; display: flex; align-items: center; justify-content: center; gap: 8px;
    color: var(--white); font-weight: 700; font-size: 20px; letter-spacing: .3px; white-space: nowrap; }
  .brand-mark .dot { width: 13px; height: 13px; border-radius: 50%; background: var(--white); flex: none; }
  .card--front .brand-mark { left: 0; right: 0; top: 128px; font-size: 28px; }
  .card--back .brand-mark { left: 24px; width: 176px; top: 131px; }

  .front-web { position: absolute; left: 0; right: 0; top: 244px; text-align: center; color: var(--accent); font-size: 18px; }

  .contact { position: absolute; left: 222px; top: 0; width: 266px; }
  .name { position: absolute; top: 66px; font-size: 17px; color: var(--accent); text-transform: uppercase; white-space: nowrap; }
  .role { position: absolute; top: 86px; font-size: 11.5px; color: var(--white); white-space: nowrap; }
  .mobile { position: absolute; top: 103px; font-size: 11.5px; color: var(--white); }
  .email { position: absolute; top: 117px; font-size: 10.5px; color: var(--white); white-space: nowrap; }
  .address { position: absolute; top: 152px; font-size: 11.5px; color: var(--ink); white-space: nowrap; }
  .phones { position: absolute; top: 171px; font-size: 11px; color: var(--ink); white-space: nowrap; }
  .phones b, .office-email b { font-weight: 400; color: var(--white); }
  .office-email { position: absolute; top: 185px; font-size: 10.5px; color: var(--ink); white-space: nowrap; }
  .web { position: absolute; top: 225px; font-size: 12px; color: var(--white); font-weight: 500; white-space: nowrap; }

  .licence { position: absolute; left: 38px; top: 254px; display: flex; align-items: center; gap: 14px; color: var(--white); font-size: 13px; }
  .member-badge { width: 22px; height: 18px; background: var(--white); display: flex; align-items: center; justify-content: center; }
  .member-badge span { width: 14px; height: 11px; background: var(--badge); border-radius: 3px; }
</style>
</head>
<body>

<section class="card card--front">
  <div class="brand-mark"><span class="dot"></span>Vantor Ridge</div>
  <p class="front-web">www.vantorridgesecurity-example.com.au</p>
</section>

<section class="card card--back card--gregory">
  <div class="info-band"></div>
  <div class="brand-mark"><span class="dot"></span>Vantor Ridge</div>
  <div class="contact">
    <p class="name">Gregory Okafor</p>
    <p class="role">Manager</p>
    <p class="mobile">0437 215 640</p>
    <p class="email">gregory@vantorridgesecurity-example.com.au</p>
    <p class="address">612 Wattlebend Rd, Coffs Harbour NSW 2450</p>
    <p class="phones"><b>T:</b> +61 2 6621 4093 <b>F:</b> +61 2 6621 4058</p>
    <p class="office-email"><b>E:</b> admin@vantorridgesecurity-example.com.au</p>
    <p class="web">www.vantorridgesecurity-example.com.au</p>
  </div>
  <div class="licence"><span class="member-badge"><span></span></span>ML 738204519</div>
</section>

<section class="card card--back card--darren">
  <div class="info-band"></div>
  <div class="brand-mark"><span class="dot"></span>Vantor Ridge</div>
  <div class="contact">
    <p class="name">Darren Okafor</p>
    <p class="role">Security Advisor / Director</p>
    <p class="mobile">0451 307 984</p>
    <p class="email">darren@vantorridgesecurity-example.com.au</p>
    <p class="address">612 Wattlebend Rd, Coffs Harbour NSW 2450</p>
    <p class="phones"><b>T:</b> +61 2 6621 4093 <b>F:</b> +61 2 6621 4058</p>
    <p class="office-email"><b>E:</b> admin@vantorridgesecurity-example.com.au</p>
    <p class="web">www.vantorridgesecurity-example.com.au</p>
  </div>
  <div class="licence"><span class="member-badge"><span></span></span>ML 738204519</div>
</section>

<section class="card card--back card--generic">
  <div class="info-band"></div>
  <div class="brand-mark"><span class="dot"></span>Vantor Ridge</div>
  <div class="contact">
    <p class="address">612 Wattlebend Rd, Coffs Harbour NSW 2450</p>
    <p class="phones"><b>T:</b> +61 2 6621 4093 <b>F:</b> +61 2 6621 4058</p>
    <p class="office-email"><b>E:</b> admin@vantorridgesecurity-example.com.au</p>
    <p class="web">www.vantorridgesecurity-example.com.au</p>
  </div>
  <div class="licence"><span class="member-badge"><span></span></span>ML 738204519</div>
</section>

</body>
</html>
```